Successful Health Company Needs a Face Lift

We need a beautiful new design for our existing, online health supplements business.

Most of the elements are already there, but we need your sophistication and style.

The 3 pages that need your magic touch are:
Home page:
http://www.vitabrook.co.uk

Multiple Product pages. e.g:
http://www.vitabrook.co.uk/health-issues/major-organs/skin-hair-nails.html

Single Product pages. e.g:
http://www.vitabrook.co.uk/l-arginine-500-mg.html

Please have a look around.

This is a bilingual site, so all text (except logo) needs to be easily changed/translated. If photoshop files can be provided where we can simply translate the text layer of a graphic, that is acceptable. Please note that Greman words are generally longer than English.

Appearance:
The over all look should be open, light, uplifting and sophisticated.

The Home Page in detail:
We are largely happy with the category boxes in the centre column although you may restyle these if you wish.
The header, left menu and right column don't hang together and need your skills.

Logo:
We would like you to enhance our logo, but please note the 'S' and circle are used on many product labels, so we can't go too far from this just now.
(Product label example: http://www.vitabrook.co.uk/black-walnut-tincture-from-green-hull.html)

Header:
This needs to imply health and be light and stylish without it taking up valuable room.

Left Menu:
This is a multi-layer concertina menu. It is hard to see where your are within it. It needs to be made more clear and easy to navigate, maybe by using indentation and or better colour choices.
Please show it expanded and condensed in your design proposals.
(Extended menu example: http://www.vitabrook.co.uk/health-issues/female-health/thrush.html)

Multiple Product pages in detail
Please style the the brief descriptions, which must contain bullet points, price, add to basket and learn more.

Single Product pages in detail
The design and layout of this page needs to include all the elements currently there, including price, Qty, Add to Basket button, size and article number.

The static blocks on the right column will appear on these single product pages and need to suit the design well. They should not over-power the central content of the page.
Updates

Thank you all for participating.

Please note that what we are looking for is a more stylish and attractive version of what we already have.  The elements are all there.  We are not looking for a new concept.

We are happy for designers to switch images for better ones, work with colour ways, alter proportions and insert the elements in our brief.

We do not want to add banners, large images etc.  We want our customers to be familiar with what they see, and to be impressed with how much better the pages hang together.  They should not think they've landed at a new company.

We do want to see how the left menu looks when extended to show 2nd and 3rd tier menu titles.
We will also want to see how the design works for a multiple product page like this: http://www.vitabrook.co.uk/supplement-type/anti-microbials.html
as well as a single product page like this:  http://www.vitabrook.co.uk/black-walnut-extract.html

Some adjustment to the 'VitaBrook' logo is also an option and the graphic has been attached. 

Thank you for your careful attention to our brief.

Malcolm.
pp Reinald

Project Deadline Extended
Reason: Due to unanticipated travel arrangements, the company director will only be available to make final decisions on Monday the 19th of March. Please continue updating submissions as we are in touch. Thank you for your understanding.

Target Market(s)

Health conscious women 70% men 30% aged 40 to 65 and health practitioners.

Industry/Entity Type

Health

Requirements
Must have
• Please include in the Header:
UK and German flags
Facebook, dig, +1, twitter, linked in, stumble upon
Padlock/SSL security/secure transaction
Practitioner helpline/ orders phone number
Paypal/Credit card logo

Please include in right column:
Clinician Corner
Mercury Free Dentistry
Shopping Basket
Storefronts for Clinicians

Please include in either Header or Right Column
Same day dispatch
Money back warranty

```html
<!DOCTYPE html>
<html lang="en">
<head>
<meta charset="utf-8">
<title>VitaBrook Enterprises – Home</title>
<link href="https://fonts.googleapis.com/css2?family=Questrial&display=swap" rel="stylesheet">
<style>
:root{
  --blue:#1a7fe0;
  --blue-dark:#0b5cc4;
  --blue-light:#4fb0f5;
  --sky:#dff0fc;
  --band:#9fd0f4;
  --cyan:#2aa9e8;
  --magenta:#d21c8a;
  --link:#1a6fd0;
  --ink:#444;
  --white:#fff;
}
*{box-sizing:border-box;margin:0;padding:0}
html,body{width:983px;height:1200px;overflow:hidden;background:#fff}
body{font-family:"Questrial",sans-serif;color:var(--ink);position:relative}
.page{position:absolute;inset:0;width:983px;height:1200px;background:linear-gradient(#f4faff,#e4f2fc 60%,#d7ecfa)}
.abs{position:absolute}

/* header */
.header{left:0;top:0;width:983px;height:164px;background:linear-gradient(90deg,#fff,#f4f9fe 40%,#eaf4fc);border-top:4px solid #c7dff5}
.logo-name{left:28px;top:60px;font-size:40px;line-height:44px;color:var(--cyan);letter-spacing:1px}
.logo-sub{left:170px;top:106px;font-size:10px;letter-spacing:3.5px;color:var(--magenta)}
.team{left:360px;top:8px;width:346px;height:156px;background:linear-gradient(90deg,#eef2f5 0%,#e6d8cc 12%,#f7f8f9 22%,#e2cfc1 32%,#fafafa 45%,#ead6c6 52%,#f6f7f8 64%,#e4d2c4 78%,#eef1f4 90%,#e3e8ec 100%)}
.pill{top:125px;height:27px;width:110px;border-radius:14px;background:linear-gradient(#3aa0f0,var(--blue-dark));color:#fff;font-size:14px;display:flex;align-items:center;justify-content:center;gap:7px;border:2px solid #fff;box-shadow:0 1px 3px rgba(0,0,0,.3)}
.social{left:722px;top:23px;width:151px;height:33px;border:1px solid #bbb;border-radius:3px;background:#f4f4f4;display:flex;gap:4px;align-items:center;justify-content:center}
.social span{width:20px;height:20px;border-radius:3px;background:var(--blue)}
.social span:first-child{background:#888}
.flag{top:30px;width:27px;height:20px}
.padlock{left:720px;top:72px}
.phone{left:760px;top:66px;font-size:27px;color:var(--magenta);letter-spacing:1px}
.cards{left:760px;top:97px;display:flex;gap:7px}
.cards span{width:34px;height:18px;border-radius:3px;background:#ccc}
.search{left:720px;top:127px;width:234px;height:28px;border:2px solid #7fb8ea;border-radius:3px;background:#fff;font-size:14px;color:#888;padding:4px 12px}
.search svg{position:absolute;right:8px;top:4px}

/* nav */
.navband{left:0;top:164px;width:983px;height:75px;background:linear-gradient(#c4e4fa,var(--band));box-shadow:0 6px 10px rgba(80,120,160,.25)}
.nav{left:41px;top:190px;display:flex;gap:17px;font-size:17px;color:#333}
.nav .active{color:var(--blue);position:relative}
.nav .active::after{content:"";position:absolute;left:50%;top:24px;margin-left:-5px;border:5px solid transparent;border-bottom-color:var(--blue)}
.badges{left:722px;top:174px;display:flex;gap:3px}
.badge{width:55px;height:55px;border-radius:4px;background:linear-gradient(#4b9df0,#0c3fa8);border:2px solid #fff;color:#ffd84a;font-size:8px;text-align:center;display:flex;align-items:flex-end;justify-content:center;padding-bottom:4px;line-height:1.05}

/* left menu */
.menu{left:43px;top:276px;width:177px}
.menu li{list-style:none;height:26.8px;display:flex}
.menu .lbl{flex:1;height:22px;background:linear-gradient(#5bb5f7,var(--blue));color:#222;font-size:11.5px;padding:4px 14px;border-left:3px solid #9cd0f7;box-shadow:0 2px 2px rgba(0,0,0,.15);white-space:nowrap}
.menu .arr{width:24px;height:22px;background:#e6f1fb;border-top:3px solid var(--blue);display:flex;align-items:center;justify-content:center}
.news{left:43px;top:663px;width:177px;height:128px;background:var(--sky);border-bottom:5px solid var(--blue)}
.news h3{background:var(--blue);color:#fff;font-weight:normal;font-size:16px;text-align:right;padding:3px 6px;height:26px}
.news p{color:var(--cyan);font-size:12px;padding:8px 7px}
.news .field{margin:0 8px;height:22px;background:#fff;border:1px solid #ccc;font-size:8px;color:#666;padding:5px 7px}
.news .btn{display:block;margin:9px auto 0;width:68px;height:20px;border-radius:3px;background:var(--blue-dark);color:#fff;font-size:10px;text-align:center;line-height:20px}

/* category boxes */
.cat{width:240px;height:138px;background:#fff;box-shadow:0 1px 3px rgba(0,0,0,.25)}
.cat h2{height:24px;background:linear-gradient(#38a2f5,var(--blue));color:#fff;font-weight:normal;font-size:15px;text-align:right;padding:3px 13px;white-space:nowrap}
.cat .pic{position:absolute;left:0;top:24px;width:130px;height:109px}
.cat ul{position:absolute;right:13px;top:44px;list-style:none;text-align:right;font-size:9.5px;line-height:15.6px;color:var(--link);white-space:nowrap}
.cat::after{content:"";position:absolute;left:0;bottom:0;width:100%;height:5px;background:linear-gradient(90deg,var(--blue),#8a3ad0 60%,var(--magenta))}

/* right column */
.side{left:753px;width:201px;background:#fff;border-bottom:4px solid var(--blue)}
.side h3{height:23px;background:linear-gradient(#38a2f5,var(--blue));color:#fff;font-weight:normal;font-size:14px;text-align:right;padding:3px 8px}
.side .txt{position:absolute;left:13px;font-size:9.5px;line-height:11.5px;color:var(--blue-dark)}
.side .pic{position:absolute;right:0;top:23px;width:84px}
.hl{color:var(--magenta)}
.findbtn{display:inline-block;margin-top:7px;padding:4px 7px;background:var(--blue-dark);color:#fff;border-radius:3px;font-size:9px}

/* footer */
.footlinks{left:0;width:983px;top:1053px;text-align:center;font-size:10px;color:#555;word-spacing:2px}
.footlinks span{margin:0 4px}
.footlinks .on{color:var(--blue)}
.bottom{left:0;top:1081px;width:983px;height:119px;background:linear-gradient(#cfe6f8,#a9d3f4);font-size:7.3px;color:#555;text-align:center;padding:24px 120px 0;line-height:9px}
.bottom p{margin-bottom:14px}
</style>
</head>
<body>
<div class="page">

  <header class="abs header">
    <div class="abs logo-name">VitaBrook</div>
    <div class="abs logo-sub">ENTERPRISES</div>

    <div class="abs team" role="img" aria-label="Photo of a smiling team of four health practitioners in white coats"></div>
    <div class="abs pill" style="left:477px">
      <svg width="15" height="13" viewBox="0 0 15 13"><path d="M0 1h3l2 7h8l2-5H4" fill="none" stroke="#fff" stroke-width="1.6"/><circle cx="6" cy="11" r="1.4" fill="#fff"/><circle cx="12" cy="11" r="1.4" fill="#fff"/></svg>My Basket</div>
    <div class="abs pill" style="left:596px">
      <svg width="11" height="14" viewBox="0 0 11 14"><rect x="0" y="6" width="11" height="8" rx="1" fill="#fff"/><path d="M2.5 6V4a3 3 0 0 1 6 0v2" fill="none" stroke="#fff" stroke-width="1.8"/></svg>Login</div>

    <div class="abs social" aria-label="Social sharing"><span></span><span></span><span></span><span></span><span></span></div>
    <svg class="abs flag" style="left:891px" viewBox="0 0 27 20" aria-label="German"><rect width="27" height="7" fill="#111"/><rect y="7" width="27" height="6" fill="#d00"/><rect y="13" width="27" height="7" fill="#fc0"/></svg>
    <svg class="abs flag" style="left:927px" viewBox="0 0 27 20" aria-label="English"><rect width="27" height="20" fill="#1a3b8a"/><path d="M0 0L27 20M27 0L0 20" stroke="#fff" stroke-width="4"/><path d="M0 0L27 20M27 0L0 20" stroke="#c8102e" stroke-width="1.4"/><path d="M13.5 0v20M0 10h27" stroke="#fff" stroke-width="6"/><path d="M13.5 0v20M0 10h27" stroke="#c8102e" stroke-width="3.4"/></svg>
    <svg class="abs padlock" width="32" height="44" viewBox="0 0 32 44" aria-label="Secure transaction"><path d="M7 20V12a9 9 0 0 1 18 0v8" fill="none" stroke="#9a9a9a" stroke-width="4"/><rect x="1" y="19" width="30" height="24" rx="3" fill="#e0a820"/><rect x="1" y="19" width="30" height="6" fill="#f2c84a"/></svg>
    <div class="abs phone">01632 - 960 412</div>
    <div class="abs cards" aria-label="Accepted payment methods"><span></span><span></span><span></span><span></span><span></span></div>
    <div class="abs search">Search
      <svg width="20" height="20" viewBox="0 0 20 20"><circle cx="12" cy="8" r="6" fill="none" stroke="#2a8ae0" stroke-width="2"/><path d="M8 12L2 18" stroke="#2a8ae0" stroke-width="3"/></svg>
    </div>
  </header>

  <div class="abs navband"></div>
  <nav class="abs nav"><span class="active">Home</span><span>Detox</span><span>Hydration</span><span>Suplements</span><span>Your Health Issues</span></nav>
  <div class="abs badges">
    <div class="badge">Founded on<br>1996</div>
    <div class="badge">100%<br>Secure</div>
    <div class="badge">Money Back<br>Guarantee</div>
    <div class="badge">Sameday<br>Dispatch</div>
  </div>

  <ul class="abs menu">
    <li><span class="lbl">A To Z</span><span class="arr"><svg width="10" height="12"><path d="M1 1l8 5-8 5z" fill="#fff" stroke="#222" stroke-width="1.6"/></svg></span></li>
    <li><span class="lbl">Supplement Type</span><span class="arr"><svg width="10" height="12"><path d="M1 1l8 5-8 5z" fill="#fff" stroke="#222" stroke-width="1.6"/></svg></span></li>
    <li><span class="lbl">Your Health Issues</span><span class="arr"><svg width="10" height="12"><path d="M1 1l8 5-8 5z" fill="#fff" stroke="#222" stroke-width="1.6"/></svg></span></li>
    <li><span class="lbl">Expert Product Lines</span><span class="arr"><svg width="10" height="12"><path d="M1 1l8 5-8 5z" fill="#fff" stroke="#222" stroke-width="1.6"/></svg></span></li>
    <li><span class="lbl">Detox &amp; Cleansing</span><span class="arr"><svg width="10" height="12"><path d="M1 1l8 5-8 5z" fill="#fff" stroke="#222" stroke-width="1.6"/></svg></span></li>
    <li><span class="lbl">Hydration &amp; Water</span><span class="arr"><svg width="10" height="12"><path d="M1 1l8 5-8 5z" fill="#fff" stroke="#222" stroke-width="1.6"/></svg></span></li>
    <li><span class="lbl">Natural Body Care</span><span class="arr"><svg width="10" height="12"><path d="M1 1l8 5-8 5z" fill="#fff" stroke="#222" stroke-width="1.6"/></svg></span></li>
    <li><span class="lbl">Sport &amp; Fitness</span><span class="arr"><svg width="10" height="12"><path d="M1 1l8 5-8 5z" fill="#fff" stroke="#222" stroke-width="1.6"/></svg></span></li>
    <li><span class="lbl">Health Technology</span><span class="arr"><svg width="10" height="12"><path d="M1 1l8 5-8 5z" fill="#fff" stroke="#222" stroke-width="1.6"/></svg></span></li>
    <li><span class="lbl">Household Products</span><span class="arr"><svg width="10" height="12"><path d="M1 1l8 5-8 5z" fill="#fff" stroke="#222" stroke-width="1.6"/></svg></span></li>
    <li><span class="lbl">Laboratory Tests</span><span class="arr"><svg width="10" height="12"><path d="M1 1l8 5-8 5z" fill="#fff" stroke="#222" stroke-width="1.6"/></svg></span></li>
    <li><span class="lbl">Books &amp; Education</span><span class="arr"><svg width="10" height="12"><path d="M1 1l8 5-8 5z" fill="#fff" stroke="#222" stroke-width="1.6"/></svg></span></li>
    <li><span class="lbl">New &amp; Special Offer</span><span class="arr"><svg width="10" height="12"><path d="M1 1l8 5-8 5z" fill="#fff" stroke="#222" stroke-width="1.6"/></svg></span></li>
  </ul>

  <section class="abs news">
    <h3>Newsletter</h3>
    <p>Sign Up for Our Newsletter</p>
    <div class="field">Please Enter Your Email Here</div>
    <span class="btn">Subscribe</span>
  </section>

  <section class="abs cat" style="left:238px;top:276px"><h2>Digestion</h2>
    <div class="pic" role="img" aria-label="Photo of a woman holding her stomach" style="background:linear-gradient(#f3e3d8,#fafafa)"></div>
    <ul><li>Constipation</li><li>Candida</li><li>Irritable Bowel</li><li>Wind</li></ul></section>
  <section class="abs cat" style="left:495px;top:276px"><h2>Pain</h2>
    <div class="pic" role="img" aria-label="Photo of a man's bare back with lower back pain" style="background:linear-gradient(90deg,#c89a7c,#e8cbb6)"></div>
    <ul style="top:50px"><li>Back Pain</li><li>Joint and Bone</li><li>Headache</li><li>Period Pain</li></ul></section>

  <section class="abs cat" style="left:238px;top:430px"><h2>Weight Loss</h2>
    <div class="pic" role="img" aria-label="Photo of a slim waist with a tape measure" style="background:linear-gradient(90deg,#3a2e2a,#e2c2a8 60%,#f6f6f6)"></div>
    <ul style="top:56px"><li>Without Dieting</li><li>Suplements</li><li>Sugar Metabolism</li></ul></section>
  <section class="abs cat" style="left:495px;top:430px"><h2>Male &amp; Female Health</h2>
    <div class="pic" role="img" aria-label="Illustration of silver male and female symbols" style="background:radial-gradient(circle at 50% 55%,#9a9a9a,#fff 70%)"></div>
    <ul style="top:34px"><li>Breast Health</li><li>Menopause</li><li>Menstruation</li><li>Erectile Disfunction</li><li>Hair Lost</li><li>Prostate Health</li></ul></section>

  <section class="abs cat" style="left:238px;top:584px"><h2>Detox</h2>
    <div class="pic" role="img" aria-label="Photo of fresh herbs in a wooden mortar" style="background:linear-gradient(#fff,#9bb37a 55%,#7a5535)"></div>
    <ul style="top:42px"><li>Heavy Metal Detox</li><li>Parasite Cleanse</li><li>Kidney Cleanse</li><li>Liver Cleanse</li><li>Colon Cleanse</li></ul></section>
  <section class="abs cat" style="left:495px;top:584px"><h2>Body Care</h2>
    <div class="pic" role="img" aria-label="Photo of a relaxed woman with a lily" style="background:linear-gradient(90deg,#bfdcee,#f4e4dc 60%,#fff)"></div>
    <ul style="top:42px"><li>Anti Aging</li><li>Cosmetics</li><li>Skin Range</li><li>Face &amp; Mouth</li><li>Hair Care</li></ul></section>

  <section class="abs cat" style="left:238px;top:740px"><h2>Brain Health</h2>
    <div class="pic" role="img" aria-label="Illustration of a brain lifting dumbbells" style="background:radial-gradient(circle at 45% 45%,#e7a9a0,#fff 65%)"></div>
    <ul style="top:41px"><li>Memory</li><li>Headaches</li><li>Cognitive Function</li><li>Mood &amp; Sleep</li></ul></section>
  <section class="abs cat" style="left:495px;top:740px"><h2>Water &amp; Hydration</h2>
    <div class="pic" role="img" aria-label="Photo of a splash of clear water" style="background:radial-gradient(ellipse at 50% 65%,#8fc6e0,#fff 65%)"></div>
    <ul style="top:54px"><li>Water Filtration</li><li>Electrolytes</li><li>Super-Hydration</li></ul></section>

  <section class="abs cat" style="left:238px;top:895px"><h2>Health Devices</h2>
    <div class="pic" role="img" aria-label="Photo of a laptop with a stethoscope reaching out of the screen" style="background:linear-gradient(135deg,#fff,#c9d4de 50%,#333 90%)"></div>
    <ul style="top:40px"><li>Zapping</li><li>Cardiovascular</li><li>Ozone</li><li>Allergy Test</li></ul></section>
  <section class="abs cat" style="left:495px;top:895px"><h2>Cardiovascular</h2>
    <div class="pic" role="img" aria-label="Illustration of a torso with a blue heart puzzle piece" style="background:radial-gradient(circle at 45% 40%,#2a7ac0,#c0553c 55%,#f0d8c8)"></div>
    <ul style="top:49px"><li>Blood Pressure</li><li>Cholesterol</li><li>Heart &amp; Arteries</li></ul></section>

  <aside class="abs side" style="top:276px;height:138px"><h3>Practitioner Help</h3>
    <div class="txt" style="top:36px">PLEASE CALL :<br>01632 - 960 412<br><span class="hl" style="display:block;margin-top:5px">Or</span><span class="findbtn">Find Practioner</span></div>
    <div class="pic" role="img" aria-label="Photo of a female doctor with a stethoscope" style="height:108px;background:linear-gradient(90deg,#fff,#dde8f0 50%,#b9cfe0)"></div></aside>
  <aside class="abs side" style="top:409px;height:118px"><h3>My Basket</h3>
    <div class="txt" style="top:48px;width:95px">You have no item on your shopping basket</div>
    <div class="pic" role="img" aria-label="Illustration of a turquoise shopping basket" style="top:28px;height:80px;width:90px;right:6px;background:radial-gradient(circle,#2cc6df,#fff 72%)"></div></aside>
  <aside class="abs side" style="top:540px;height:118px"><h3>Mercury Free</h3>
    <div class="txt" style="top:43px;width:100px">Mercury Free Dentist in UK &amp; Ireland. A comprehensive list is <span class="hl">Available Here</span></div>
    <div class="pic" role="img" aria-label="Photo of a woman with a bright smile" style="height:91px;background:linear-gradient(90deg,#fff,#f0d6c4 40%,#c89376)"></div></aside>
  <aside class="abs side" style="top:672px;height:118px"><h3>Clinician Corner</h3>
    <div class="txt" style="top:53px">Contact a Natural<br>Health <span class="hl">Practitioner</span></div>
    <div class="pic" role="img" aria-label="Photo of a nurse holding a clipboard" style="height:91px;background:linear-gradient(90deg,#fff,#e8dccf 45%,#6e9ccc)"></div></aside>

  <div class="abs footlinks"><span class="on">About Us</span><span>Search Terms</span><span>Advanced Search</span><span>Terms &amp; Conditions</span><span>Privacy Policy</span><span>Contact Us</span></div>

  <footer class="abs bottom">
    <p>Kidney Pain Kidney Stones Kidney Disease Symptoms Colon Cleanse Digestive Enzymes Digestive Enzymes Supplement Healing Principles Herbal Remedies Herbal Remedies for Anxiety Herbal Remedies for Constipation Herbal Remedies for Depression Herbal Remedies for Menopause Bloated Stomach Health Shops Digestra What is Mercury Free Dentistry?</p>
    <p>© 2010 VitaBrook Enterprises. All Rights Reserved.</p>
    <p>Please note: This information is provided for educational purposes only. Medical advice is neither implied nor intended.<br>Please consult a health professional for medical advice.</p>
  </footer>
</div>
</body>
</html>
```